Professional Modern Website Design

We are a premium IT services provider to the financial industry based in London. Our company is called Velmar our current holding page is www.velmar.co.uk. We require a new website to match our new corporate identity. This project is for the design phase only. Development will be handled in-house. I have attached examples of wire frames we have developed (although open to suggestions for improvement) Our brand document that should demonstrate current brand, inc how we communicate to potential clients and finally mostly completed web-content.
We are looking for designers that can create something that sets us apart from our competitors.
Target Market(s)
IT Decision makers in Finance companies such as; hedge funds, private investment banks etc
Industry/Entity Type
Financial
Number of Pages Required
5+ page
Requirements
Must have
- hexagon elements in the design, unique design.
Nice to have
- Blog and social media feeds
Should not have
- Should not resemble a downloaded template

```html
<!DOCTYPE html>
<html lang="en">
<head>
<meta charset="utf-8">
<title>Velmar — IT Services</title>
<link href="https://fonts.googleapis.com/css2?family=Roboto:wght@300;400;700;900&display=swap" rel="stylesheet">
<style>
:root{
  --night:#1d2533;
  --night-deep:#0f141d;
  --orange:#f47c20;
  --amber:#fbb817;
  --ink:#333;
  --grey-text:#5b5b5b;
  --muted:#777;
  --bar:#474747;
  --hex-dark:#5a5a5a;
  --panel:#eeeeee;
  --white:#fff;
  --map-base:#e8e2d6;
}
*{margin:0;padding:0;box-sizing:border-box}
html,body{width:970px;height:1200px;overflow:hidden;background:var(--white)}
body{position:relative;font-family:"Roboto",Arial,sans-serif;color:var(--ink)}
.abs{position:absolute}

/* hero */
.hero{left:0;top:0;width:970px;height:347px;background:linear-gradient(180deg,#27384a 0%,#1b2432 45%,#2a2a30 75%,#14161c 100%)}
.brand{left:40px;top:16px;display:flex;flex-direction:column;align-items:flex-start;gap:8px}
.brand-mark{width:30px;height:30px;background:var(--orange)}
.brand-name{color:#fff;font-size:10px;letter-spacing:4px;font-weight:400}
.nav{top:23px;left:444px;display:flex;gap:0;font-size:13px;color:#fff}
.nav span{position:absolute;white-space:nowrap}
.nav .active{color:var(--amber)}
.dropdown{left:535px;top:50px;width:265px;height:151px;background:#f4f4f4;padding:5px 10px;font-size:12px;color:#444}
.dropdown::before{content:"";position:absolute;top:-6px;left:38px;border:6px solid transparent;border-top:0;border-bottom-color:#f4f4f4}
.dropdown li{list-style:none;height:29px;line-height:29px}
.dropdown li.current{color:#111}
.hero-kicker{left:38px;top:215px;color:#fff;font-size:16px;font-weight:400}
.hero-title{left:38px;top:234px;color:#fff;font-size:33px;font-weight:900}
.read-more{left:36px;top:278px;width:118px;height:31px;border:1px solid var(--orange);color:#fff;font-size:16px;line-height:29px;text-align:center}
.dots{left:455px;top:318px;display:flex;gap:6px}
.dots i{width:10px;height:10px;border-radius:50%;background:#888}
.dots i:first-child{background:#fff}
.accent-band{left:0;top:347px;width:970px;height:14px;background:linear-gradient(90deg,var(--amber),var(--orange))}

/* services */
.services{left:0;top:361px;width:970px;height:483px;background:linear-gradient(180deg,#e6e6e6 0%,#f4f4f4 60%,#fff 100%)}
.section-title{top:47px;width:970px;text-align:center;font-size:20px;font-weight:900;letter-spacing:6px;color:#333}
.section-sub{top:74px;width:970px;text-align:center;font-size:20px;font-weight:300;color:#555}
.service{width:220px;text-align:center}
.service svg{display:block;margin:0 auto}
.service h3{font-size:17px;font-weight:400;color:#444;margin-top:10px}
.service p{font-size:12px;line-height:19.4px;color:#666;margin-top:4px}

/* contact bar */
.contact-bar{left:0;top:844px;width:970px;height:75px;background:var(--bar);color:#fff}
.contact-item{top:18px;display:flex;gap:10px}
.contact-item .dot{width:17px;height:17px;border-radius:50%;background:var(--amber);margin-top:1px}
.contact-item .tag{width:17px;height:14px;background:var(--amber);transform:rotate(40deg);margin-top:2px}
.contact-item b{display:block;font-weight:400;font-size:15px}
.contact-item span{font-size:13px}
.social{top:28px;font-size:14px;color:var(--amber);font-weight:700}
.divider{left:716px;top:10px;width:1px;height:52px;background:#777}
.feed{left:734px;top:12px;width:225px;font-size:12.5px;font-style:italic;line-height:18px;color:#ddd}
.center-hex{left:423px;top:810px}
.center-name{left:423px;top:903px;width:125px;text-align:center;color:#ccc;font-size:11px;letter-spacing:4px}
.center-mark{left:467px;top:855px;width:37px;height:37px;background:#b9b9b9}

/* offices */
.offices{left:0;top:919px;width:970px;height:184px;background:linear-gradient(90deg,#e3e3e3,#f7f7f7)}
.office{top:44px;width:182px;font-size:12px;color:#777;line-height:19.4px;letter-spacing:.3px}
.office h4{font-weight:400;font-size:12.5px;color:#444;padding-bottom:4px;border-bottom:1px solid #ccc;margin-bottom:14px}
.map{left:590px;top:919px;width:380px;height:181px;background:linear-gradient(135deg,#e4dccd,#efe9dd 60%,#dfe7d3)}
</style>
</head>
<body>

<header class="hero abs">
  <div class="brand abs"><div class="brand-mark"></div><div class="brand-name">VELMAR</div></div>
  <nav class="nav abs">
    <span style="left:0">ABOUT</span>
    <span class="active" style="left:93px">SERVICES</span>
    <span style="left:202px">PARTERNS</span>
    <span style="left:311px">CLIENTS</span>
    <span style="left:410px">CONTACT</span>
  </nav>
  <ul class="dropdown abs">
    <li>Data centre &amp; Infracstructure</li>
    <li class="current">Support, managed &amp; professional services</li>
    <li>Voice and data</li>
    <li>Hosting and data</li>
    <li>Security and IRM</li>
  </ul>
  <div class="hero-kicker abs">CONSECTETUR ADIPISCING ELIT</div>
  <div class="hero-title abs">LOREM IPSUM</div>
  <div class="read-more abs">Read more</div>
  <div class="dots abs"><i></i><i></i><i></i><i></i></div>
</header>
<div role="img" aria-label="Night city skyline photograph behind the hero text" class="abs" style="left:0;top:150px;width:970px;height:197px;background:linear-gradient(180deg,rgba(20,24,32,0) 0%,rgba(40,36,34,.6) 60%,rgba(16,18,24,.9) 100%);pointer-events:none;z-index:0"></div>
<div class="accent-band abs"></div>

<section class="services abs">
  <h2 class="section-title abs">LOREM IPSUM DOLOR SIT</h2>
  <p class="section-sub abs">Amet consectetur adipiscing elit. Pellentesque mi dui</p>

  <svg width="0" height="0" class="abs"><defs>
    <linearGradient id="hexFill" x1="0" y1="0" x2="0" y2="1"><stop offset="0" stop-color="#fff"/><stop offset="1" stop-color="#e2e2e2"/></linearGradient>
    <symbol id="hex" viewBox="0 0 150 172">
      <polygon points="75,2 148,44 148,128 75,170 2,128 2,44" fill="url(#hexFill)" stroke="#ececec" stroke-width="3"/>
      <polygon points="50,152 100,152 75,168" fill="#c8c8c8"/>
    </symbol>
  </defs></svg>

  <div class="service abs" style="left:21px;top:132px">
    <svg width="148" height="170" viewBox="0 0 150 172">
      <use href="#hex"/>
      <g fill="#6d6d6d"><path d="M50 52h30l12 12v40H50z"/><rect x="57" y="74" width="24" height="4" fill="#eee"/><rect x="57" y="83" width="16" height="4" fill="#eee"/><circle cx="88" cy="100" r="11" fill="none" stroke="#6d6d6d" stroke-width="5"/><path d="M95 107l10 10" stroke="#6d6d6d" stroke-width="6"/></g>
    </svg>
    <h3>Lorem ipsum dolor sit</h3>
    <p>amet consectetur adipiscing elit. Pellentesque mi dui, fermentum ut ligula eu, commodo tincidunt nunc. In elementum imperdiet erat, iaculis fringilla risus varius at</p>
  </div>
  <div class="service abs" style="left:256px;top:132px">
    <svg width="148" height="170" viewBox="0 0 150 172">
      <use href="#hex"/>
      <g fill="none" stroke="#6d6d6d" stroke-width="5"><rect x="44" y="79" width="18" height="28"/><rect x="70" y="57" width="16" height="50"/><rect x="94" y="87" width="16" height="20"/></g>
      <rect x="40" y="112" width="74" height="5" fill="#6d6d6d"/>
    </svg>
    <h3>Lorem ipsum dolor sit</h3>
    <p>amet consectetur adipiscing elit. Pellentesque mi dui, fermentum ut ligula eu, commodo tincidunt nunc. In elementum imperdiet erat, iaculis fringilla risus varius at</p>
  </div>
  <div class="service abs" style="left:491px;top:132px">
    <svg width="148" height="170" viewBox="0 0 150 172">
      <use href="#hex"/>
      <rect x="38" y="56" width="76" height="50" fill="none" stroke="#6d6d6d" stroke-width="5"/>
      <rect x="70" y="108" width="12" height="8" fill="#6d6d6d"/><rect x="60" y="115" width="32" height="5" fill="#6d6d6d"/>
    </svg>
    <h3>Lorem ipsum dolor sit</h3>
    <p>amet consectetur adipiscing elit. Pellentesque mi dui, fermentum ut ligula eu, commodo tincidunt nunc. In elementum imperdiet erat, iaculis fringilla risus varius at</p>
  </div>
  <div class="service abs" style="left:726px;top:132px">
    <svg width="148" height="170" viewBox="0 0 150 172">
      <use href="#hex"/>
      <g fill="#6d6d6d"><circle cx="54" cy="64" r="10"/><circle cx="98" cy="64" r="10"/><path d="M36 94c0-14 8-20 18-20s16 6 16 20z"/><path d="M82 94c0-14 6-20 16-20s18 6 18 20z"/><circle cx="76" cy="76" r="12"/><path d="M56 116c0-18 9-26 20-26s20 8 20 26z"/></g>
    </svg>
    <h3>Lorem ipsum dolor sit</h3>
    <p>amet consectetur adipiscing elit. Pellentesque mi dui, fermentum ut ligula eu, commodo tincidunt nunc. In elementum imperdiet erat, iaculis fringilla risus varius at</p>
  </div>
</section>

<section class="offices abs">
  <div class="office abs" style="left:59px">
    <h4>LONDON OFFICE</h4>
    18 HARLOW ROW,<br>WESTBURY, LONDON W2 7QN<br>T:+44 20 7946 0183<br>E:INFO@VELMAR.CO.UK
  </div>
  <div class="office abs" style="left:265px;width:226px">
    <h4>ESSEX OFFICE</h4>
    9 MILL YARD, KESTREL<br>LANE, COLBROOK, ESSEX CB4 2RT<br>T:+44 20 7946 0182<br>E:INFO@VELMAR.CO.UK
  </div>
</section>
<div class="map abs" role="img" aria-label="Street map showing the London office location"></div>

<section class="contact-bar abs">
  <div class="contact-item abs" style="left:39px"><div class="dot"></div><div><b>SUPPORT</b><span>+44 20 7946 0182</span></div></div>
  <div class="contact-item abs" style="left:239px"><div class="tag"></div><div><b>SALES</b><span>+44 20 7946 0183</span></div></div>
  <div class="social abs" style="left:578px">Follows</div>
  <div class="social abs" style="left:650px">Chirp</div>
  <div class="divider abs"></div>
  <p class="feed abs">#Pellentesque mi dui, fermentum ut ligula eu, @commodo tincidunt nunc. fermentum ut ligula eu.</p>
</section>
<svg class="center-hex abs" width="125" height="143" viewBox="0 0 125 143"><polygon points="62.5,0 125,36 125,107 62.5,143 0,107 0,36" fill="var(--hex-dark)"/></svg>
<div class="center-mark abs"></div>
<div class="center-name abs">VELMAR</div>

</body>
</html>
```